Letterhead to Prospective Clients

Create a letterhead (word & canva) that I will use to send letters to prospective clients and also include the Coralwood Estate Partners Logo, My Contact Details and Interchangeable "Suburb". Use the same font and colour pallete

Maris Dulworth | "Suburb" Specialist - Harwick & Surrounds
Mobile: 0417 862 095
Email: MD@CoralwoodEstatePartners.com.au

```html
<!DOCTYPE html>
<html lang="en">
<head>
<meta charset="utf-8">
<title>Coralwood Estate Partners – Letterhead</title>
<link href="https://fonts.googleapis.com/css2?family=Josefin+Sans:wght@300&family=Outfit:wght@400;600&display=swap" rel="stylesheet">
<style>
  :root {
    --navy: #00153a;
    --gold: #c9a27e;
    --paper: #ffffff;
    --backdrop: #838488;
    --ink-light: #e8ecf3;
  }
  * { margin: 0; padding: 0; box-sizing: border-box; }
  html, body { width: 1200px; height: 1200px; overflow: hidden; }
  body {
    background: var(--backdrop);
    font-family: "Outfit", sans-serif;
    position: relative;
  }
  .letterhead {
    position: absolute;
    left: 167px; top: 40px;
    width: 866px; height: 1120px;
    background: var(--paper);
  }
  .header-band {
    position: absolute; left: 0; top: 0;
    width: 100%; height: 153px;
    background: var(--navy);
  }
  .header-rule {
    position: absolute; left: 0; top: 159px;
    width: 100%; height: 4px;
    background: var(--gold);
  }
  .brand-name {
    position: absolute; left: 68px; top: 60px;
    font-family: "Josefin Sans", sans-serif;
    font-weight: 300;
    font-size: 20px;
    letter-spacing: 2px;
    color: var(--paper);
    text-transform: uppercase;
    line-height: 26px;
    white-space: nowrap;
  }
  .contact {
    position: absolute; right: 72px; top: 27px;
    text-align: right;
    color: var(--paper);
    white-space: nowrap;
  }
  .contact-name {
    font-weight: 600;
    font-size: 18px;
    letter-spacing: 5px;
    color: var(--gold);
    text-transform: uppercase;
    line-height: 22px;
  }
  .contact-role {
    font-size: 11.5px;
    line-height: 18px;
  }
  .contact-line {
    display: flex; justify-content: flex-end; align-items: center;
    gap: 10px;
    font-size: 12.5px;
    letter-spacing: 0.3px;
    height: 25px;
  }
  .contact-icon { width: 17px; height: 17px; flex: none; }
  .footer-rule {
    position: absolute; left: 0; top: 1080px;
    width: 100%; height: 4px;
    background: var(--gold);
  }
  .footer-band {
    position: absolute; left: 0; top: 1088px;
    width: 100%; height: 32px;
    background: var(--navy);
  }
  .footer-name {
    position: absolute; right: 68px; top: 9px;
    font-family: "Josefin Sans", sans-serif;
    font-weight: 300;
    font-size: 12px;
    letter-spacing: 1.5px;
    color: var(--ink-light);
    text-transform: uppercase;
  }
</style>
</head>
<body>
  <main class="letterhead">
    <header class="header-band">
      <div class="brand-name">Coralwood Estate Partners</div>
      <div class="contact">
        <div class="contact-name">Maris Dulworth</div>
        <div class="contact-role">"Suburb" Specialist – Harwick &amp; Surrounds</div>
        <div class="contact-line">
          <span>0417 862 095</span>
          <svg class="contact-icon" viewBox="0 0 20 20" aria-hidden="true">
            <circle cx="10" cy="10" r="8.8" fill="none" stroke="#c9a27e" stroke-width="1.4"/>
            <rect x="7" y="4.8" width="6" height="10.4" rx="1.2" fill="none" stroke="#c9a27e" stroke-width="1.2"/>
            <line x1="9" y1="13.3" x2="11" y2="13.3" stroke="#c9a27e" stroke-width="1"/>
          </svg>
        </div>
        <div class="contact-line">
          <span>MD@CoralwoodEstatePartners.com.au</span>
          <svg class="contact-icon" viewBox="0 0 20 20" aria-hidden="true">
            <circle cx="10" cy="10" r="9.5" fill="#c9a27e"/>
            <rect x="5" y="6.5" width="10" height="7" rx="0.8" fill="#00153a"/>
            <polyline points="5.4,7 10,10.6 14.6,7" fill="none" stroke="#c9a27e" stroke-width="1"/>
          </svg>
        </div>
        <div class="contact-line">
          <span>Ashgrove Rise, Kellow Bay, Tarrin &amp; Mt Verity</span>
          <svg class="contact-icon" viewBox="0 0 20 20" aria-hidden="true">
            <circle cx="10" cy="10" r="9.5" fill="#c9a27e"/>
            <path d="M5 10 L10 5.5 L15 10 H13.4 V14.5 H6.6 V10 Z" fill="#00153a"/>
            <rect x="9" y="11.4" width="2" height="3.1" fill="#c9a27e"/>
          </svg>
        </div>
      </div>
    </header>
    <div class="header-rule"></div>

    <div class="footer-rule"></div>
    <footer class="footer-band">
      <div class="footer-name">Coralwood</div>
    </footer>
  </main>
</body>
</html>
```